Modern Design Business Card industrial maintenance company

Business card design for Company named Brookvale Equipment Services

Target Market(s)

Industrial

Industry/Entity Type

Maintenance and repair

Contact Information for Business Card

Place holder for address, office phone, mobile number and email

Requirements
Must have
• Clean modern look
Nice to have
• N/a

```html
<!DOCTYPE html>
<html lang="en">
<head>
<meta charset="utf-8">
<title>Brookvale Equipment Services – Business Card</title>
<link rel="stylesheet" href="https://fonts.googleapis.com/css2?family=Montserrat:wght@400;500;700&display=swap">
<style>
  :root {
    --backdrop: #3a3a3a;
    --ink: #0b0b0b;
    --paper: #ffffff;
    --steel: #9a9a9a;
  }
  * { margin: 0; padding: 0; box-sizing: border-box; }
  html, body { width: 1200px; height: 689px; overflow: hidden; }
  body {
    background: var(--backdrop);
    font-family: "Montserrat", sans-serif;
    position: relative;
  }
  .card {
    position: absolute;
    top: 196px;
    width: 520px;
    height: 298px;
    border-radius: 16px;
    overflow: hidden;
    box-shadow: 0 14px 30px rgba(0,0,0,.45);
  }
  .card--back { left: 50px; background: var(--ink); }
  .card--front { left: 630px; background: var(--paper); }

  .brand { position: absolute; display: flex; align-items: center; }
  .brand__dot { border-radius: 50%; flex: none; }
  .brand__name {
    font-weight: 700;
    text-transform: uppercase;
    line-height: 1.1;
    letter-spacing: .08em;
  }
  .card--back .brand { left: 0; right: 0; top: 0; bottom: 0; justify-content: center; gap: 12px; }
  .card--back .brand__dot { width: 30px; height: 30px; border: 2px solid var(--paper); }
  .card--back .brand__name { color: var(--paper); font-size: 15px; }

  .wave { position: absolute; left: 0; top: 0; }

  .card--front .brand {
    left: 34px; top: 46px; width: 200px;
    flex-direction: column; gap: 12px;
  }
  .card--front .brand__dot { width: 68px; height: 68px; border: 4px solid var(--ink); }
  .card--front .brand__name { color: var(--ink); font-size: 16px; text-align: center; }

  .divider {
    position: absolute; left: 262px; top: 36px;
    width: 1px; height: 140px; background: var(--ink);
  }
  .contact { position: absolute; left: 282px; top: 30px; color: var(--ink); }
  .contact__name { font-size: 24px; font-weight: 700; line-height: 1.1; }
  .contact__role { font-size: 11px; font-weight: 500; margin-bottom: 8px; }
  .contact__address { font-size: 11px; line-height: 1.35; margin-bottom: 6px; }
  .contact__list { list-style: none; font-size: 11px; }
  .contact__list li { display: flex; align-items: center; gap: 7px; line-height: 1.55; }
  .contact__list svg { width: 11px; height: 11px; flex: none; }
</style>
</head>
<body>

<section class="card card--back" aria-label="Card back">
  <div class="brand">
    <span class="brand__dot"></span>
    <span class="brand__name">Brookvale<br>Equipment Services</span>
  </div>
</section>

<section class="card card--front" aria-label="Card front">
  <svg class="wave" width="520" height="298" viewBox="0 0 520 298" aria-hidden="true">
    <path d="M0,264 C130,252 200,206 330,200 C430,196 490,190 520,146 L520,298 L0,298 Z" fill="var(--steel)"/>
    <path d="M0,274 C130,262 205,216 335,210 C435,206 492,200 520,160 L520,298 L0,298 Z" fill="var(--ink)"/>
  </svg>

  <div class="brand">
    <span class="brand__dot"></span>
    <span class="brand__name">Brookvale<br>Equipment<br>Services</span>
  </div>

  <div class="divider"></div>

  <div class="contact">
    <p class="contact__name">Dana Whitfield</p>
    <p class="contact__role">Managing Director</p>
    <p class="contact__address">18 Harbor Mill Lane<br>Lakeford, OH 44012 USA</p>
    <ul class="contact__list">
      <li>
        <svg viewBox="0 0 24 24" aria-hidden="true"><path fill="var(--ink)" d="M6.6 10.8a15 15 0 0 0 6.6 6.6l2.2-2.2c.3-.3.7-.4 1-.2 1.1.4 2.3.6 3.6.6.6 0 1 .4 1 1V20c0 .6-.4 1-1 1A17 17 0 0 1 3 4c0-.6.4-1 1-1h3.5c.6 0 1 .4 1 1 0 1.3.2 2.5.6 3.6.1.3 0 .7-.2 1z"/></svg>
        555 210 4400
      </li>
      <li>
        <svg viewBox="0 0 24 24" aria-hidden="true"><rect x="6" y="2" width="12" height="20" rx="2" fill="none" stroke="var(--ink)" stroke-width="2"/><circle cx="12" cy="18" r="1.2" fill="var(--ink)"/></svg>
        555 318 7726
      </li>
      <li>
        <svg viewBox="0 0 24 24" aria-hidden="true"><path fill="var(--ink)" d="M2 5h20v14H2z"/><path fill="none" stroke="var(--paper)" stroke-width="1.6" d="M2.5 5.5 12 13l9.5-7.5"/></svg>
        info@brookvale-es.com
      </li>
    </ul>
  </div>
</section>

</body>
</html>
```